Allied Health Clinic needs catchy poster ad for lightbox

We need a catchy and effective poster designed for our retail lightbox which is in a busy corridor. We are a multi disciplinary sports injury clinic offering a range of allied health services. Established in 1999. We need people to understand our business identity and services clearly. I have come up with a very rough idea as far as what I think the copy should contain. The picture is an example of what image I am trying to convey to the potential client. I am not a designer clearly. We specialise in treating difficult problems.
Size of the poster is 451mm x 741mm at 300dpi. We will then blow the image up to double this size which will be good enough resolution for the printing.

Target Market(s)

White collar professionals - male and female, active 20-50 range

Industry/Entity Type

Healthcare

Font styles to use
Sans Serif

Requirements
Nice to have
• Easy to read, polished, nice tie in to my logo colours

```html
<!DOCTYPE html>
<html lang="en">
<head>
<meta charset="utf-8">
<title>Corefield Physiotherapy – Lightbox Poster</title>
<link rel="stylesheet" href="https://fonts.googleapis.com/css2?family=Anton&family=Oswald:wght@500;600;700&family=Libre+Baskerville:wght@700&display=swap">
<style>
  :root {
    --green: #86c440;
    --blue: #3aa9f2;
    --ink: #1b1b1b;
    --charcoal: #4a4a4a;
    --paper: #ffffff;
    --navy: #1f2a48;
  }
  * { margin: 0; padding: 0; box-sizing: border-box; }
  html, body { width: 848px; height: 1200px; overflow: hidden; background: var(--paper); }
  .poster { position: relative; width: 848px; height: 1200px; overflow: hidden; background: var(--paper); }

  .rings { position: absolute; inset: 0; }

  .brand { position: absolute; left: 92px; top: 88px; display: flex; align-items: center; gap: 22px; }
  .brand-dot { width: 64px; height: 64px; border-radius: 50%; background: var(--green); }
  .brand-name { font-family: "Oswald", sans-serif; font-weight: 600; font-size: 32px; letter-spacing: 1px; color: var(--charcoal); line-height: 1.1; }

  .headline { position: absolute; left: 55px; top: 214px; font-family: "Anton", sans-serif; font-weight: 400; font-size: 80px; line-height: 1; letter-spacing: 6px; color: var(--ink); }
  .tagline { position: absolute; left: 55px; top: 292px; font-family: "Oswald", sans-serif; font-weight: 700; font-size: 66px; line-height: 1; color: var(--blue); letter-spacing: 0.5px; }
  .since { position: absolute; left: 55px; top: 368px; font-family: "Libre Baskerville", serif; font-weight: 700; font-size: 25px; line-height: 1.45; color: var(--ink); }

  .athlete { position: absolute; left: 150px; top: 448px; width: 428px; height: 549px; border-radius: 200px 200px 0 0;
    background: linear-gradient(180deg, #2a3556 0%, #2a3556 42%, #e9e9ea 52%, #d9d9da 64%, #1f2a48 78%, #1a1a1a 100%); opacity: .9; }

  .services { position: absolute; left: 593px; top: 738px; list-style: none; font-family: "Oswald", sans-serif; font-weight: 700; font-size: 25px; line-height: 1.18; color: var(--ink); }
  .services li { position: relative; padding-left: 22px; margin-bottom: 8px; }
  .services li::before { content: ""; position: absolute; left: 0; top: 10px; width: 10px; height: 10px; border-radius: 50%; background: var(--blue); }

  .info-band { position: absolute; left: 0; top: 997px; width: 848px; height: 143px; background: var(--charcoal); color: var(--paper); font-family: "Oswald", sans-serif; font-weight: 700; }
  .directions { position: absolute; left: 50px; top: 14px; line-height: 1; }
  .directions .small { display: block; font-size: 44px; }
  .directions .large { display: block; font-size: 56px; margin-top: 4px; }
  .contact { position: absolute; left: 573px; top: 14px; line-height: 1; }
  .contact .label { display: block; font-size: 56px; }
  .contact .phone { display: block; font-size: 44px; margin-top: 8px; }

  .web-band { position: absolute; left: 0; top: 1140px; width: 848px; height: 60px; background: var(--green); display: flex; align-items: center; justify-content: center;
    font-family: "Oswald", sans-serif; font-weight: 600; font-size: 19px; letter-spacing: 7.5px; color: var(--ink); }
</style>
</head>
<body>
<main class="poster">
  <svg class="rings" width="848" height="1200" viewBox="0 0 848 1200" aria-hidden="true">
    <g transform="translate(535 877) scale(1.012 0.871)">
      <circle r="436" fill="none" stroke="var(--green)" stroke-width="92"/>
      <circle r="360" fill="none" stroke="var(--blue)" stroke-width="18"/>
    </g>
  </svg>

  <header class="brand">
    <span class="brand-dot"></span>
    <span class="brand-name">Corefield Physiotherapy<br>&amp; Sports Injury Clinic</span>
  </header>

  <h1 class="headline">INJURY EXPERTS</h1>
  <h2 class="tagline">TRUSTED BY ATHLETES</h2>
  <p class="since">SUCCESSFULLY TREATING DIFFICULT<br>INJURIES SINCE 1999</p>

  <div class="athlete" role="img" aria-label="Photograph of a footballer in a navy jersey and white shorts volleying a ball"></div>

  <ul class="services">
    <li>SPORTS<br>PHYSIOTHERAPY</li>
    <li>CHIROPRACTIC</li>
    <li>MASSAGE</li>
    <li>PODIATRY</li>
    <li>EXERCISE<br>PHYSIOLOGY</li>
  </ul>

  <section class="info-band">
    <p class="directions"><span class="small">TAKE LIFTS TO</span><span class="large">LEVEL 8</span></p>
    <p class="contact"><span class="label">CALL US:</span><span class="phone">8450 2716</span></p>
  </section>

  <footer class="web-band">www.corefieldphysioclinic.com.au</footer>
</main>
</body>
</html>
```